Motivational Quotes Poster Series

This is a 3 poster design series for Ridgeway Haul Academy. The size of each poster should be 18 inches wide and 24 inches tall. The goal of these posters is to serve as motivational "signs" to be hung in the office area for the employees (not customers). These employees are instructors/teachers, teaching students how to drive semi trucks. While each design is a separate poster and design, we're posting as 1 project because we'd like some continuity between the series. Below we'll break down the details of all 3 posters...

Poster #1
Text that must appear on poster - "If You Want The Best Out Of Each Student" and "Give The Best Of You!" Note: While this text must appear on the poster, you can arrange in the layout as you see fit. For example, first line could be at top of poster and second line on bottom.

Poster #2
Text that must appear on poster - "Invest In People" and "Change Someone's Life" (same notes apply as in 1st poster)

Poster #3
Text that must appear on poster - "Today Is..." and "Just Another Day For You" and "The Most Important Day In Their Life" Note: This can be laid out on the poster however you see fit, but each phrase needs to be separate and it needs to flow.

Target Market(s)

Truck Driver Training Instructors - These are middle-aged, mostly male, masculine type personalities.

Industry/Entity Type

Training

Requirements
Must have
• Must have noted text from description
Must have working files (ie - PSD, EPS, AI, etc) provided
Must have common theme between each poster in series
Must have easy to read font and layout
Must have product dimensions of 18 inches (width) by 24 inches (height). If design uses full dimensions please include quarter inch bleed.
Nice to have
• Nice to have a trucking theme...related to trucking industry, but not over the top. Example - This could mean subtle injection of background tire tracks, but by no means are tire tracks required.

For inspiration, you can visit the site at http://www.ridgewayhaulacademy.com. While you can use the colors of the site/logo, you can still branch out between each poster to try new colors within reason.

Note: While we've attached the logo to this project, it COULD be used but doesn't HAVE to be included in the design. The logo IS NOT a focal point. The phrases in the poster ARE the focal point.

```html
<!DOCTYPE html>
<html lang="en">
<head>
<meta charset="UTF-8">
<title>Today Is… — Ridgeway Haul Academy Motivational Poster</title>
<link rel="stylesheet" href="https://fonts.googleapis.com/css2?family=Oswald:wght@600;700&display=swap">
<style>
  :root {
    --asphalt: #1b1b1b;
    --lane-paint: #9a9a9a;
    --signal-amber: #f7ab3c;
  }
  * { margin: 0; padding: 0; box-sizing: border-box; }
  html, body {
    width: 900px;
    height: 1200px;
    overflow: hidden;
    background: var(--asphalt);
  }
  .poster {
    position: relative;
    width: 900px;
    height: 1200px;
    overflow: hidden;
    background: var(--asphalt);
    font-family: "Oswald", "Arial Narrow", sans-serif;
    color: var(--signal-amber);
  }
  .road-surface {
    position: absolute;
    inset: 0;
    width: 900px;
    height: 1200px;
  }
  .phrase {
    position: absolute;
    list-style: none;
  }
  .phrase-line {
    display: block;
    white-space: nowrap;
    font-weight: 600;
  }
  .phrase-line--small {
    font-size: 45px;
    line-height: 45px;
  }
  .phrase-line--large {
    font-size: 84px;
    line-height: 79px;
    font-weight: 700;
  }
  .phrase--yours { left: 66px; top: 163px; }
  .phrase--yours .phrase-line--small:first-child { margin-bottom: 22px; }
  .phrase--yours .phrase-line--small:last-child { margin-top: 17px; font-size: 54px; line-height: 54px; }

  .phrase--theirs { left: 522px; top: 502px; }
  .phrase--theirs .phrase-line--small { font-size: 54px; line-height: 54px; }
  .phrase--theirs .phrase-line--small:first-child { margin-bottom: 10px; }
  .phrase--theirs .phrase-line--small:last-child { margin-top: 19px; }
</style>
</head>
<body>
<main class="poster">
  <svg class="road-surface" viewBox="0 0 900 1200" aria-hidden="true">
    <defs>
      <filter id="asphalt-grain" x="0" y="0" width="100%" height="100%">
        <feTurbulence type="fractalNoise" baseFrequency="0.9" numOctaves="2" seed="4" result="grain"/>
        <feColorMatrix in="grain" type="saturate" values="0" result="mono"/>
        <feComponentTransfer in="mono" result="soft">
          <feFuncA type="linear" slope="0.14"/>
        </feComponentTransfer>
        <feComposite in="soft" in2="SourceGraphic" operator="over"/>
      </filter>
      <filter id="paint-grain" x="0" y="0" width="100%" height="100%">
        <feTurbulence type="fractalNoise" baseFrequency="1.1" numOctaves="2" seed="9" result="grain"/>
        <feColorMatrix in="grain" type="saturate" values="0" result="mono"/>
        <feComponentTransfer in="mono" result="soft">
          <feFuncA type="linear" slope="0.55"/>
        </feComponentTransfer>
        <feComposite in="soft" in2="SourceGraphic" operator="atop"/>
      </filter>
    </defs>
    <rect class="road-asphalt" width="900" height="1200" fill="#1b1b1b" filter="url(#asphalt-grain)"/>
    <g class="lane-divider" fill="#9a9a9a" filter="url(#paint-grain)">
      <rect x="414" y="0" width="72" height="69"/>
      <rect x="414" y="178" width="72" height="845"/>
      <rect x="414" y="1104" width="72" height="96"/>
    </g>
  </svg>

  <h1 class="phrase phrase--yours">
    <span class="phrase-line phrase-line--small">Today Is...</span>
    <span class="phrase-line phrase-line--large">Just</span>
    <span class="phrase-line phrase-line--large">Another</span>
    <span class="phrase-line phrase-line--large">Day</span>
    <span class="phrase-line phrase-line--small">For You</span>
  </h1>

  <p class="phrase phrase--theirs">
    <span class="phrase-line phrase-line--small">The</span>
    <span class="phrase-line phrase-line--large">Most</span>
    <span class="phrase-line phrase-line--large">Important</span>
    <span class="phrase-line phrase-line--large">Day</span>
    <span class="phrase-line phrase-line--small">In Their Life</span>
  </p>
</main>
</body>
</html>
```